FINANCIAL MANAGEMENT COMPANY LOGO

LOGO, BUSINESS CARD & STATIONERY

NEW FINANCIAL MANAGEMENT COMPANY

name: ORVEL Financial Management Pty Ltd
abn xx xxx xxx xxx
address: (not yet available)
Telephone: (not yet available)

Strategic Financial Planning and Management Company

- Superannuation
- SMSF (Own Fund)
- Retail/Industry Funds (fund controlled)

- Personal Wealth
- Planning
- Forcasting
- Portfolio Management

- Future Generations
- Strategy
- Structural Implimenation and Management

- Risk Insurance
- Analysis
- Implimentation
- Review

NOTES:
I would like to project professionalism, security and personal care.
Comforting, warm colours

Name on Business card:

Maren Toll
FPRB Authorised Financial Strategist

THANK YOU FOR THE SUBMISSIONS .......
I WOULD LIKE TO SEE EARTHY AND  RELAXED TONES WITH AN UNDERSTANDING OF AN 'ALL INCLUSIVE  & CARING' FEEL.
REALLY APPRECIATE ALL THE  IDEAS SO FAR....

Target Market(s)

Middle aged, reasonably wealthy, successful,

Industry/Entity Type

Security

Logo Text

ORVEL Financial Management Pty Ltd

Logo styles of interest
Abstract Logo
Requirements
Must have
• business card to carry full deatils of company and it's services (as previously described in this brief)
Nice to have
• Logo to be easily recognised on all stationey and advertising boards

```html
<!DOCTYPE html>
<html lang="en">
<head>
<meta charset="utf-8">
<title>Strategic Financial Planning and Management Company</title>
<link rel="stylesheet" href="https://fonts.googleapis.com/css2?family=Rokkitt:wght@400;700&family=Belleza&display=swap">
<style>
  :root {
    --card-khaki: #a8a07f;
    --frame-brown: #3d210c;
    --ink-brown: #3a1f0c;
    --leaf-green: #7b8a2c;
    --note-grey: #6a6753;
    --cream: #e8dec6;
  }
  * { margin: 0; padding: 0; box-sizing: border-box; }
  html, body { width: 1200px; height: 686px; overflow: hidden; background: var(--card-khaki); }
  .card {
    position: relative;
    width: 1200px;
    height: 686px;
    background: var(--card-khaki);
    font-family: "Rokkitt", Georgia, serif;
    color: var(--ink-brown);
  }
  .frame {
    position: absolute;
    left: 26px; top: 24px;
    width: 1149px; height: 639px;
    border: 3px solid var(--frame-brown);
  }
  .service-list {
    position: absolute;
    top: 56px;
    list-style: none;
    font-size: 27px;
    line-height: 45.5px;
    letter-spacing: -0.4px;
  }
  .service-list li { position: relative; padding-left: 35px; }
  .service-list li::before {
    content: "";
    position: absolute;
    left: 0; top: 19px;
    width: 24px; height: 9px;
    background: var(--leaf-green);
    border-radius: 0 100% 0 100%;
  }
  .service-list .heading { font-weight: 700; }
  .service-list .wrap { padding-left: 35px; }
  .service-list .wrap::before { display: none; }
  .col-super { left: 44px; }
  .col-wealth { left: 343px; }
  .col-future { left: 618px; }
  .col-risk { left: 944px; }

  .aged-care {
    position: absolute;
    left: 188px; top: 252px;
    padding-left: 46px;
    font-size: 37px;
    line-height: 46px;
    letter-spacing: -0.5px;
  }
  .aged-care::before {
    content: "";
    position: absolute;
    left: 0; top: 18px;
    width: 38px; height: 13px;
    background: var(--leaf-green);
    border-radius: 0 100% 0 100%;
  }
  .aged-care-note {
    position: absolute;
    left: 226px; top: 303px;
    font-size: 25px;
    color: var(--note-grey);
    letter-spacing: -0.3px;
  }
  .dome {
    position: absolute;
    left: 0; top: 0;
    width: 1200px; height: 686px;
  }
  .tagline {
    position: absolute;
    left: 0; width: 1200px;
    top: 516px;
    text-align: center;
    font-family: "Belleza", "Optima", sans-serif;
    font-size: 35px;
    line-height: 48px;
    letter-spacing: 0.6px;
    color: var(--cream);
  }
</style>
</head>
<body>
<div class="card">
  <svg class="dome" width="1200" height="686" viewBox="0 0 1200 686" aria-hidden="true">
    <path d="M235 663 A367 255 0 0 1 969 663 Z" fill="#3e200b"/>
  </svg>
  <div class="frame"></div>

  <ul class="service-list col-super">
    <li class="heading">Superannuation</li>
    <li>SMSF (Own Fund)</li>
    <li>Retail/Industry Funds</li>
    <li class="wrap">(fund controlled)</li>
  </ul>
  <ul class="service-list col-wealth">
    <li class="heading">Personal Wealth</li>
    <li>Planning</li>
    <li>Forcasting</li>
    <li>Portfolio Management</li>
  </ul>
  <ul class="service-list col-future">
    <li class="heading">Future Generations</li>
    <li>Strategy</li>
    <li>Structural Implimenation</li>
    <li class="wrap">and Management</li>
  </ul>
  <ul class="service-list col-risk">
    <li class="heading">Risk Insurance</li>
    <li>Analysis</li>
    <li>Implimentation</li>
    <li>Review</li>
  </ul>

  <p class="aged-care">Aged Care Financial Assessment Assistance and Advice</p>
  <p class="aged-care-note">Focused advice, coverage and mapping of our clients financial position.</p>

  <p class="tagline">Strategic Financial Planning<br>and Management Company</p>
</div>
</body>
</html>
```